Tending Our Garden eBook Cover Design

I want to deisgn a cover for my eBook (FRONT COVER) and the title is:

What I Grew From a Single Spark. And Why It Matters
By KT Dorran

TITLE CHANGED TO: UNDER THE WILLOW TREE; WHERE I FOUND MY QUIET STRENGTH AND WHERE YOU MIGHT TOO

The color palette is attached. Along with some photos options of me. Along with the ebook in WORD Document. My website is www.KTDorranLive.example. You can use a different color palette if you think it is best

Target Market(s)

women who look to build a personal brand

Industry/Entity Type

health and wellness

Requirements
Must have
• the title
Nice to have
• use my picture on the cover; but that is optional
Should not have
• any men

```html
<!DOCTYPE html>
<html lang="en">
<head>
<meta charset="utf-8">
<title>Under the Willow Tree — eBook Cover</title>
<link rel="stylesheet" href="https://fonts.googleapis.com/css2?family=Krona+One&family=Montserrat:wght@800;900&display=swap">
<style>
  :root {
    --rose-outer: #d48b9d;
    --rose-outer-light: #f0b5c5;
    --blush: #f6c5d4;
    --rose-mid: #d98da1;
    --rose-deep: #c46b7f;
    --wine: #62272d;
    --white: #ffffff;
  }
  html, body {
    margin: 0;
    padding: 0;
    width: 788px;
    height: 1200px;
    overflow: hidden;
    background: var(--rose-outer);
  }
  .cover {
    position: relative;
    width: 788px;
    height: 1200px;
    background: linear-gradient(135deg, var(--rose-outer) 0%, var(--rose-outer-light) 55%, var(--rose-outer) 100%);
  }
  .cover-art {
    position: absolute;
    inset: 0;
    display: block;
  }
  .title-display { font-family: "Krona One", "Arial Black", sans-serif; }
  .title-pill { font-family: "Montserrat", "Arial Black", sans-serif; font-weight: 900; }
  .author-photo {
    position: absolute;
    left: 118px;
    top: 414px;
    width: 620px;
    height: 680px;
    border-radius: 200px 200px 20px 20px;
    background: linear-gradient(180deg, #3a2a2c 0%, #1d1718 45%, #141112 100%);
  }
</style>
</head>
<body>
<main class="cover">
  <svg class="cover-art" width="788" height="1200" viewBox="0 0 788 1200" xmlns="http://www.w3.org/2000/svg">
    <defs>
      <clipPath id="panel-clip">
        <rect x="21" y="32" width="745" height="1136" rx="36"/>
      </clipPath>
      <linearGradient id="diagonal-fill" x1="0" y1="0" x2="1" y2="1">
        <stop offset="0" stop-color="#cf7c90"/>
        <stop offset="1" stop-color="#eaa9ba"/>
      </linearGradient>
      <linearGradient id="footer-fill" x1="0" y1="0" x2="1" y2="0">
        <stop offset="0" stop-color="#c26a7e"/>
        <stop offset="0.5" stop-color="#e9a6b7"/>
        <stop offset="1" stop-color="#c26a7e"/>
      </linearGradient>
    </defs>

    <!-- panel -->
    <g class="panel" clip-path="url(#panel-clip)">
      <rect x="21" y="32" width="745" height="1136" fill="var(--blush)"/>
      <polygon points="766,328 766,1168 21,1168 21,976" fill="url(#diagonal-fill)"/>
      <!-- title band -->
      <rect x="21" y="106" width="745" height="104" fill="var(--blush)"/>
      <rect x="21" y="110" width="745" height="96" fill="var(--wine)"/>
      <!-- footer band -->
      <rect x="21" y="1094" width="745" height="74" fill="url(#footer-fill)"/>
    </g>
    <rect x="21" y="32" width="745" height="1136" rx="36" fill="none" stroke="var(--wine)" stroke-width="4"/>

    <!-- title -->
    <text class="title-display" x="393" y="93" text-anchor="middle" font-size="46" fill="var(--rose-deep)" textLength="530" lengthAdjust="spacingAndGlyphs">UNDER THE</text>
    <text class="title-display" x="393" y="196" text-anchor="middle" font-size="88" fill="var(--blush)" textLength="660" lengthAdjust="spacingAndGlyphs">WILLOW TREE</text>
    <text class="title-display" x="393" y="255" text-anchor="middle" font-size="31" fill="var(--rose-deep)" textLength="485" lengthAdjust="spacingAndGlyphs">WHERE I FOUND MY</text>

    <rect x="46" y="269" width="696" height="68" rx="22" fill="var(--wine)" stroke="var(--rose-deep)" stroke-width="3"/>
    <text class="title-pill" x="393" y="325" text-anchor="middle" font-size="56" fill="var(--white)" textLength="640" lengthAdjust="spacingAndGlyphs">QUIET STRENGTH</text>

    <text class="title-display" x="394" y="390" text-anchor="middle" font-size="31" fill="var(--white)" textLength="540" lengthAdjust="spacingAndGlyphs">AND WHERE YOU MIGHT TOO</text>
    <text class="title-display" x="393" y="388" text-anchor="middle" font-size="31" fill="var(--rose-deep)" textLength="540" lengthAdjust="spacingAndGlyphs">AND WHERE YOU MIGHT TOO</text>

    <!-- author -->
    <text class="title-display" x="397" y="1156" text-anchor="middle" font-size="34" fill="#b45d70" textLength="350" lengthAdjust="spacingAndGlyphs">BY KT DORRAN</text>
    <text class="title-display" x="394" y="1153" text-anchor="middle" font-size="34" fill="var(--white)" textLength="350" lengthAdjust="spacingAndGlyphs">BY KT DORRAN</text>
  </svg>

  <div class="author-photo" role="img" aria-label="Portrait photo of the author, smiling, long dark hair, in a black sheer striped top with hands on hips"></div>
</main>
</body>
</html>
```